Wellness company needs a label design for a new health product

The name of the product is Verdell Drops and is part of Korvani Wellness. It allows a person to alkalize and maintain a healthy pH so their body can be at optimal health. This is a new product that will be sold in health professional offices only so it should look professional but have a cutting edge appeal. We are open to color options, keeping in mind we want to look fresh not like everyone else out there. We have the existing logo for Korvani Wellness already designed that will be needed to be incorporated into the label design. To get the Korvani Wellness logo either go to www.korvwell.example or I have attached a few files. Please contact me if you need me to send logo. Label will wrap around a bottle which will need to have room for a list of ingredients as well as suggested use.

I added a few examples of lables, the first being too basic, I would like more than that. The next two are examples of lables with added design to give it some interest but keeping it still professional. We are looking for a professional feel with an interesting edge.

A thought might be to have a muted design or soft watermark effect in the background. Thanks for all ideas
Updates

We are happy to inform you that we have guaranteed this project. Look forward to seeing your designs.

Reason: We are extending this projesct because we have guaranteed this project. Look forward to working with you.

Reason: Have not received many designs so we are extending the project. Will update more specific details hope this will help. Appreciate your help, thanks

I added two more labels that we like to give an idea what we are looking for, hope this helps.  Have not received many designs look forward to more, thanks

I added some new ideas, I look forward to seeing more designers ideas.

Reason: Waiting for some changes and possible new designs to make our decision.

Target Market(s)

Health Care profesionals, Chiropractors, Wellness Centers

Industry/Entity Type

Health

Requirements
Must have
• Korvani Wellness logo
product name: Verdell Drops
Should not have
• No people or animals

```html
<!DOCTYPE html>
<html lang="en">
<head>
<meta charset="utf-8">
<title>Verdell Drops – Label</title>
<link rel="stylesheet" href="https://fonts.googleapis.com/css2?family=Questrial&family=Roboto+Condensed:wght@400;700&family=Open+Sans:ital,wght@1,300;1,400&display=swap">
<style>
  :root{
    --bg:#dcdcdc;
    --ink:#1c1c1c;
    --muted:#555;
    --box-line:#b9b9b9;
    --yellow:#f4e81c;
    --lime:#8cc63f;
    --green:#3cb04a;
    --deep-green:#2f9a58;
    --purple:#6a2c91;
    --white:#ffffff;
  }
  *{box-sizing:border-box;margin:0;padding:0}
  html,body{width:1200px;height:900px;overflow:hidden;background:var(--bg)}
  .stage{position:relative;width:1200px;height:900px}
  .label{
    position:absolute;left:62px;top:226px;width:860px;height:358px;
    transform:scale(1.25);transform-origin:0 0;overflow:hidden;
    font-family:"Roboto Condensed",Arial,sans-serif;color:var(--ink);
  }
  .label-art{position:absolute;inset:0}
  .info-box{
    position:absolute;background:var(--white);border:1px solid var(--box-line);
    border-radius:4px;padding:3px 5px;font-size:9.2px;line-height:1.2;
  }
  .info-box h3{font-size:10.5px;font-weight:700;margin-top:1px}
  .info-box p+h3{margin-top:4px}
  .directions{left:23px;top:93px;width:222px;height:62px}
  .consumer{left:23px;top:159px;width:222px;height:105px}
  .ingredients{left:627px;top:48px;width:210px;height:80px}
  .product-info{left:627px;top:130px;width:210px;height:142px}
  .maker{left:627px;top:278px;width:210px;height:30px}
  .ingredient-list{list-style:none}
  .ingredient-list li{display:flex;justify-content:space-between;padding-right:18px}
  .brand-name{
    position:absolute;left:322px;top:52px;
    font-family:"Questrial",sans-serif;font-size:17px;letter-spacing:.3px;
    color:#333;text-transform:uppercase;
  }
  .product-name{
    position:absolute;left:318px;top:150px;width:228px;
    font-family:"Questrial",sans-serif;color:var(--ink);text-align:right;line-height:1;
  }
  .product-name .main{display:block;font-size:52px;text-align:left}
  .product-name .sub{display:block;font-size:27px;margin-top:0}
  .tagline{
    position:absolute;left:315px;top:292px;width:230px;text-align:center;
    font-family:"Open Sans",sans-serif;font-style:italic;font-weight:300;
    font-size:11.5px;line-height:1.35;color:var(--muted);
  }
  .count{
    position:absolute;left:611px;top:324px;font-family:"Questrial",sans-serif;
    font-size:13px;color:#333;
  }
  .count .unit{color:#888}
</style>
</head>
<body>
<main class="stage">
  <section class="label">
    <svg class="label-art" width="860" height="358" viewBox="0 0 860 358" aria-hidden="true">
      <defs>
        <linearGradient id="left-wash" x1="0" y1="0" x2="1" y2="0">
          <stop offset="0" stop-color="#f4e81c"/>
          <stop offset=".22" stop-color="#b9d435"/>
          <stop offset=".5" stop-color="#6fbf43"/>
          <stop offset="1" stop-color="#3cb04a"/>
        </linearGradient>
        <linearGradient id="right-wash" x1="0" y1="0" x2="1" y2="1">
          <stop offset="0" stop-color="#2f9a58"/>
          <stop offset=".45" stop-color="#3c7f77"/>
          <stop offset="1" stop-color="#6a2c91"/>
        </linearGradient>
      </defs>
      <rect width="430" height="358" fill="url(#left-wash)"/>
      <rect x="430" width="430" height="358" fill="url(#right-wash)"/>
      <path d="M318,0 Q278,179 322,358 L360,358 Q315,179 345,0 Z" fill="#8cc63f"/>
      <path d="M608,0 C560,110 575,270 705,358 L730,358 C600,270 590,110 630,0 Z" fill="#35a66a"/>
      <path d="M330,0 Q290,179 336,358 L695,358 C570,270 560,110 615,0 Z" fill="#fff"/>
    </svg>

    <div class="info-box directions">
      <h3>Suggested Directions</h3>
      <p>Adults take as a dietary supplement; take 1-2 capsules with a glass of water 5 to 10 minutes prior to eating a main meal or starchy food, or 1 capsule before a snack.</p>
    </div>
    <div class="info-box consumer">
      <h3>Consumer Information</h3>
      <p>This product is not intended to treat, diagnose, cure or prevent any disease. Do not exceed the stated dose.</p>
      <h3>Storage</h3>
      <p>Keep container tightly closed and do not expose to excessive heat. Store out of reach and sight of children.</p>
    </div>

    <div class="brand-name">Korvani Wellness</div>
    <h1 class="product-name"><span class="main">Verdell</span><span class="sub">Drops</span></h1>
    <p class="tagline">Allows person to alkalize and maintain a healthy pH so their body can be at optimal health</p>

    <div class="info-box ingredients">
      <h3>Ingredients (per capsule)</h3>
      <ul class="ingredient-list">
        <li><span>Verra 2 Lumenbean 2250</span><span>250mg</span></li>
        <li><span>Guarana P.E. (22% Caffeine)</span><span>40mg</span></li>
        <li><span>Vitamin C (Ascorbic Acid)</span><span>150mg</span></li>
        <li><span>Chromium (Polynicotinate)</span><span>25mcg</span></li>
        <li><span>Capsule (Vegetable Cellulose)</span><span>100mg</span></li>
      </ul>
    </div>
    <div class="info-box product-info">
      <h3>Product Information</h3>
      <p>Verra 2 Carb Blocker is a natural extract that blocks the enzyme responsible for the digestion of carbohydrates. Many studies prove that low carb is an effective way to lose weight. Research also shows that Carb Blocker is a safe, effective, all natural dietary supplement that does not contain harmful stimulants. The Carb Blocker Starch-Neutraliser nutrient blocks the digestive enzyme alpha-amylase before it can convert starch into glucose therefore aiding weight loss.</p>
    </div>
    <div class="info-box maker">
      <p>Manufactured in the UK to GMP and ISO 9001 Quality Assurance for www.larkfieldlabs.example</p>
    </div>

    <p class="count">100<span class="unit">tabs</span></p>
  </section>
</main>
</body>
</html>
```